Coffee Promotion for Specialty Coffees

I need to have a poster designed to promote our coffee sales. We offer cappuccino for $3.75, Latte for $3.75, Americano for $2.00, Espresso $2.00 and Fair Trade Organic Colombian Coffee for $1.75 Med, $2.00L Large. I would like sometihng very visual that shows the coffees and also has the pricing, and includes the wording" Try our Amazing Specialty Coffees!" Our logo is attached as well

Poster size is 24" wide x 36" high

Target Market(s)

Seniors and Students in a Mall Setting

Colors

Designer to choose colors to be used in the design.

Requirements
Must have
• Graphic artwork of coffees (cappuccinos, lattes, etc). Logo included in artwork. Must be for 24"wide x 36" high poster
Nice to have
• Would like something that shows closeups of the coffees and visually sells the coffee being premium and delicious.

```html
<!DOCTYPE html>
<html lang="en">
<head>
<meta charset="utf-8">
<title>Specialty Coffees Poster</title>
<link href="https://fonts.googleapis.com/css2?family=Lobster&family=Montserrat:wght@500;600&display=swap" rel="stylesheet">
<style>
  :root {
    --page-bg: #e7e3dd;
    --parchment: #857659;
    --parchment-dark: #4b3d2c;
    --roast: #24170f;
    --bean: #4e2317;
    --bean-deep: #2a120c;
    --cream: #f4f1ec;
    --cup: #e9e4dc;
  }
  * { box-sizing: border-box; margin: 0; padding: 0; }
  html, body { width: 926px; height: 1200px; overflow: hidden; background: var(--page-bg); }
  .poster {
    position: absolute; left: 63px; top: 0; width: 800px; height: 1200px; overflow: hidden;
    background: linear-gradient(180deg, var(--parchment) 0%, #6f6148 22%, var(--parchment-dark) 38%, var(--roast) 52%, var(--bean) 66%, #3a1810 85%, var(--bean-deep) 100%);
  }
  .texture {
    position: absolute; inset: 0;
    background: radial-gradient(ellipse at 35% 18%, rgba(190,175,140,.35), transparent 55%);
  }
  .cup-photo {
    position: absolute; left: 0; top: 250px; width: 320px; height: 470px;
    background: radial-gradient(ellipse at 40% 45%, var(--cup) 0%, #cfc7bb 38%, rgba(120,100,80,.5) 62%, transparent 75%);
  }
  .bean-photo {
    position: absolute; left: 0; top: 720px; width: 800px; height: 480px;
    background: radial-gradient(ellipse at 50% 60%, rgba(110,45,30,.45), transparent 70%);
  }
  .headline-top {
    position: absolute; left: 116px; top: 70px; width: 640px;
    font-family: "Montserrat", sans-serif; font-weight: 600; font-size: 54px;
    letter-spacing: 4px; color: var(--cream); text-shadow: 0 3px 4px rgba(0,0,0,.5);
  }
  .headline-script {
    position: absolute; right: 48px; text-align: right;
    font-family: "Lobster", cursive; color: var(--cream);
    text-shadow: 0 4px 5px rgba(0,0,0,.55);
  }
  .headline-specialty { top: 130px; font-size: 118px; }
  .headline-coffees { top: 270px; font-size: 128px; }
  .menu { position: absolute; left: 330px; top: 500px; width: 420px; list-style: none; }
  .menu-item {
    display: flex; align-items: baseline; height: 47px;
    font-family: "Lobster", cursive; font-size: 31px; color: var(--cream);
    text-shadow: 0 2px 3px rgba(0,0,0,.6);
  }
  .menu-rule { flex: 1; border-bottom: 2px solid var(--cream); margin: 0 10px; transform: translateY(-6px); }
  .menu-price { width: 80px; text-align: right; }
  .house-coffee {
    position: absolute; left: 0; top: 745px; width: 800px; text-align: center;
    font-family: "Lobster", cursive; font-size: 31px; line-height: 47px; color: var(--cream);
    text-shadow: 0 2px 3px rgba(0,0,0,.6);
  }
  .brand {
    position: absolute; left: 0; top: 990px; width: 800px; text-align: center;
    font-family: "Montserrat", sans-serif; font-weight: 600; font-size: 48px;
    color: var(--cream);
  }
</style>
</head>
<body>
  <main class="poster">
    <div class="texture" role="img" aria-label="Crumpled parchment paper texture"></div>
    <div class="cup-photo" role="img" aria-label="Photograph of a steaming cup of coffee on a saucer with coffee beans"></div>
    <div class="bean-photo" role="img" aria-label="Photograph of roasted coffee beans"></div>

    <h1>
      <span class="headline-top">Try our Amazing</span>
      <span class="headline-script headline-specialty">specialty</span>
      <span class="headline-script headline-coffees">Coffees!</span>
    </h1>

    <ul class="menu">
      <li class="menu-item"><span>Cappuccino</span><span class="menu-rule"></span><span class="menu-price">$3.75</span></li>
      <li class="menu-item"><span>Latte</span><span class="menu-rule"></span><span class="menu-price">$3.75</span></li>
      <li class="menu-item"><span>Americano</span><span class="menu-rule"></span><span class="menu-price">$2.00</span></li>
      <li class="menu-item"><span>Espresso</span><span class="menu-rule"></span><span class="menu-price">$2.00</span></li>
    </ul>

    <p class="house-coffee">Fair Trade Organic Colombian<br>Coffee for $1.75 | Med $2.00L Large.</p>

    <p class="brand">Rollhaven</p>
  </main>
</body>
</html>
```